Design some Business Cards for Brindle Office Assistance

Hello Everyone! I need a business card designed. I have attached the logo and the color scheme can be found on my website at www.brindleofficehelp.com (teal as the primary color). I look forward to seeing your ideas!

```html
<!DOCTYPE html>
<html lang="en">
<head>
<meta charset="utf-8">
<title>Brindle Office Assistance – Business Cards</title>
<link href="https://fonts.googleapis.com/css2?family=Raleway:wght@300;400;500&display=swap" rel="stylesheet">
<style>
  :root {
    --teal: #3fa79e;
    --teal-deep: #2b8c84;
    --teal-light: #7cc9c1;
    --mist: #cfe9e6;
    --white: #ffffff;
    --ink: #3a3a3a;
    --grey: #7a7a7a;
    --backdrop: #eef1f1;
  }
  * { box-sizing: border-box; margin: 0; padding: 0; }
  html, body { width: 1200px; height: 912px; overflow: hidden; }
  body {
    background: var(--backdrop);
    font-family: "Raleway", Arial, sans-serif;
    position: relative;
  }
  .card {
    position: absolute;
    width: 560px;
    height: 320px;
    border-radius: 4px;
    overflow: hidden;
    background: var(--white);
    box-shadow: 0 6px 18px rgba(0,0,0,0.18);
  }
  .card-services { left: 70px; top: 110px; }
  .card-contact { left: 570px; top: 480px; }
  .card-bg { position: absolute; inset: 0; width: 100%; height: 100%; }

  .world-map {
    position: absolute;
    border-radius: 40% 45% 35% 50%;
  }
  .card-services .world-map {
    left: 60px; top: 30px; width: 330px; height: 160px;
    background: radial-gradient(ellipse at center, rgba(255,255,255,0.35), rgba(255,255,255,0.08) 70%, transparent);
  }
  .card-contact .world-map {
    left: 190px; top: 62px; width: 290px; height: 110px;
    background: radial-gradient(ellipse at center, rgba(124,201,193,0.45), rgba(124,201,193,0.12) 70%, transparent);
  }

  .service-list {
    position: absolute;
    right: 40px; top: 28px;
    list-style: none;
    color: var(--white);
    font-weight: 300;
    font-size: 18px;
    line-height: 1.3;
  }
  .website {
    position: absolute;
    right: 36px; bottom: 30px;
    font-size: 20px;
    letter-spacing: 2px;
    color: var(--ink);
  }

  .holder {
    position: absolute;
    right: 26px; top: 22px;
    text-align: right;
  }
  .holder-name { font-size: 21px; font-weight: 400; color: var(--grey); }
  .holder-title { font-size: 10px; color: var(--grey); letter-spacing: 0.5px; }

  .brand-name {
    position: absolute;
    left: 212px; top: 112px;
    font-size: 22px;
    font-weight: 500;
    color: var(--ink);
  }

  .figure-area {
    position: absolute;
    left: 48px; top: 84px;
    width: 140px; height: 148px;
    border-radius: 44% 44% 20% 20%;
    background: linear-gradient(180deg, #6b4a3a 0%, #d9a98a 38%, var(--teal) 62%, var(--teal-deep) 100%);
  }

  .contact-list {
    position: absolute;
    list-style: none;
    font-size: 12px;
    color: var(--ink);
  }
  .contact-list li { display: flex; align-items: center; gap: 9px; height: 22px; }
  .contact-left { left: 28px; top: 244px; }
  .contact-right { left: 310px; top: 192px; }
  .dot {
    width: 13px; height: 13px; border-radius: 50%;
    background: var(--ink); flex: none;
  }
  .icon { width: 15px; height: 15px; flex: none; }
</style>
</head>
<body>

<section class="card card-services">
  <svg class="card-bg" viewBox="0 0 560 320" preserveAspectRatio="none">
    <defs>
      <linearGradient id="tealFace" x1="0" y1="0" x2="1" y2="1">
        <stop offset="0" stop-color="#5bb8af"/>
        <stop offset="1" stop-color="#2f948b"/>
      </linearGradient>
    </defs>
    <rect width="560" height="320" fill="url(#tealFace)"/>
    <path d="M0 320 L0 272 C130 252 240 178 380 160 C460 150 520 158 560 164 L560 320 Z" fill="#e3e3e3"/>
    <path d="M0 320 L0 284 C130 264 240 190 380 172 C460 162 520 170 560 176 L560 320 Z" fill="var(--white)"/>
  </svg>
  <div class="world-map" role="img" aria-label="Faint world map decoration"></div>
  <ul class="service-list">
    <li>- Office Administration,</li>
    <li>- Travel Arrangements,</li>
    <li>- Project Management &amp;</li>
    <li>- Event Planning</li>
  </ul>
  <p class="website">www.brindleofficehelp.com</p>
</section>

<section class="card card-contact">
  <svg class="card-bg" viewBox="0 0 560 320" preserveAspectRatio="none">
    <path d="M0 320 L0 230 C140 230 260 190 360 150 C440 118 510 110 560 108 L560 320 Z" fill="var(--teal-light)"/>
    <path d="M0 320 L0 242 C140 242 262 204 364 164 C444 132 512 124 560 122 L560 320 Z" fill="var(--teal)"/>
  </svg>
  <div class="holder">
    <p class="holder-name">Maren Castell</p>
    <p class="holder-title">Executive Administrative Consultant</p>
  </div>
  <div class="world-map" role="img" aria-label="Faint world map decoration"></div>
  <p class="brand-name">Brindle Office Assistance</p>
  <div class="figure-area" role="img" aria-label="Illustration of an assistant holding a globe"></div>

  <ul class="contact-list contact-left">
    <li>
      <svg class="icon" viewBox="0 0 16 16"><circle cx="8" cy="8" r="7" fill="none" stroke="#3a3a3a" stroke-width="1.4"/><ellipse cx="8" cy="8" rx="3" ry="7" fill="none" stroke="#3a3a3a" stroke-width="1.2"/><path d="M1 8 H15" stroke="#3a3a3a" stroke-width="1.2"/></svg>
      brindleofficehelp.com
    </li>
    <li><span class="dot"></span>network/brindle-office-assistance</li>
    <li><span class="dot"></span>social/brindleofficehelp</li>
  </ul>

  <ul class="contact-list contact-right">
    <li>
      <svg class="icon" viewBox="0 0 16 16"><rect x="1" y="3" width="14" height="10" fill="none" stroke="#3a3a3a" stroke-width="1.4"/><path d="M1 3 L8 9 L15 3" fill="none" stroke="#3a3a3a" stroke-width="1.4"/></svg>
      info@brindleofficehelp.com
    </li>
    <li><span class="dot"></span>boards/brindleoffice</li>
    <li><span class="dot"></span>profile/+BrindleOffice</li>
  </ul>
</section>

</body>
</html>
```